Larkmoor Health- Core Values Graphic for Visual Appeal

I would like a poster that could take these written core values from our organization and create a graphic that we could use for our staff and employees. I would also like to incorporate our branding into this project. Thank you!

Target Market(s)

To helps patients and employees understand the core values of our organization

Industry/Entity Type

Healthcare

Requirements
Must have
• Match our branding
Nice to have
• Please use your creativity!
Should not have
• Overly complex/ busy

```html
<!DOCTYPE html>
<html lang="en">
<head>
<meta charset="utf-8">
<title>Larkmoor Health – Core Values</title>
<link rel="stylesheet" href="https://fonts.googleapis.com/css2?family=Ubuntu:wght@300;400;500;700&display=swap">
<style>
  :root {
    --brand-blue: #2aa9e0;
    --charcoal: #404042;
    --ink: #1f1f21;
    --paper: #ffffff;
    --coat-shade: #e4e5e8;
    --tie-blue: #5a9cf0;
  }
  * { margin: 0; padding: 0; box-sizing: border-box; }
  html, body { width: 927px; height: 1200px; overflow: hidden; background: var(--paper); }
  .poster {
    position: relative;
    width: 927px;
    height: 1200px;
    overflow: hidden;
    background: var(--paper);
    font-family: "Ubuntu", sans-serif;
  }
  .coat-photo {
    position: absolute;
    left: 372px;
    top: 0;
    width: 555px;
    height: 980px;
    background:
      linear-gradient(100deg, rgba(255,255,255,0) 62%, rgba(180,210,245,0.6) 78%, var(--tie-blue) 96%),
      linear-gradient(160deg, #ffffff 10%, var(--coat-shade) 45%, #f7f7f8 75%, #ffffff 100%);
    -webkit-mask-image: linear-gradient(90deg, transparent 0%, #000 25%);
    mask-image: linear-gradient(90deg, transparent 0%, #000 25%);
  }
  .brand {
    position: absolute;
    left: 52px;
    top: 140px;
    display: flex;
    align-items: center;
    gap: 10px;
  }
  .brand-dot {
    width: 26px;
    height: 26px;
    border-radius: 50%;
    background: var(--brand-blue);
  }
  .brand-name {
    font-weight: 700;
    font-size: 28px;
    color: var(--charcoal);
    letter-spacing: 0.2px;
  }
  .intro {
    position: absolute;
    left: 55px;
    top: 351px;
    width: 340px;
    font-weight: 500;
    font-size: 16.6px;
    line-height: 19.6px;
    color: var(--brand-blue);
  }
  .value {
    position: absolute;
    left: 0;
    width: 560px;
    height: 130px;
  }
  .value-badge {
    position: absolute;
    left: 0;
    top: 0;
    width: 140px;
    height: 92px;
  }
  .value-title {
    position: absolute;
    left: 0;
    top: 81px;
    width: 182px;
    text-align: center;
    font-weight: 500;
    font-size: 20.5px;
    color: var(--brand-blue);
  }
  .value-text {
    position: absolute;
    left: 169px;
    top: 4px;
    width: 392px;
    font-weight: 300;
    font-size: 10px;
    line-height: 14.1px;
    color: var(--ink);
  }
  .value--family { top: 506px; }
  .value--excellence { top: 665px; }
  .value--integrity { top: 824px; }
  .value--service { top: 983px; }
  .accent-dot {
    position: absolute;
    left: 629px;
    top: 847px;
    width: 172px;
    height: 172px;
    border-radius: 50%;
    background: var(--brand-blue);
  }
  .bottom-wave { position: absolute; left: 0; top: 0; }
</style>
</head>
<body>
<main class="poster">
  <div class="coat-photo" role="img" aria-label="Photo of a white doctor's coat with a blue tie and a stethoscope draped over the shoulder"></div>

  <header class="brand">
    <span class="brand-dot"></span>
    <span class="brand-name">Larkmoor Health</span>
  </header>

  <p class="intro">These core values are the spirit of who we are as a healthcare team. They guide our actions, unite us in purpose, and ensure that we provide world-class care while fostering a positive and supportive atmosphere within our team:</p>

  <section class="value value--family">
    <svg class="value-badge" viewBox="0 0 140 92" aria-hidden="true">
      <path d="M0,12 Q30,30 62,16 L62,76 Q30,62 0,80 Z" fill="var(--charcoal)"/>
      <circle cx="91" cy="46" r="41.5" fill="var(--charcoal)"/>
      <g fill="#fff">
        <circle cx="80" cy="32" r="5"/><circle cx="100" cy="32" r="5"/><circle cx="90" cy="45" r="4"/>
        <rect x="73" y="39" width="14" height="24" rx="4"/><rect x="93" y="39" width="14" height="24" rx="4"/>
        <rect x="85" y="50" width="10" height="14" rx="3"/>
      </g>
    </svg>
    <h2 class="value-title">Family</h2>
    <p class="value-text">At the heart of our mission is the commitment to provide high-quality, affordable healthcare in a comforting and uplifting family-oriented environment. Just as our community is our extended family, every patient is a cherished member of our healthcare family. We treat each individual with the same care, compassion, and respect we would offer to our own loved ones.</p>
  </section>

  <section class="value value--excellence">
    <svg class="value-badge" viewBox="0 0 140 92" aria-hidden="true">
      <path d="M0,12 Q30,30 62,16 L62,76 Q30,62 0,80 Z" fill="var(--charcoal)"/>
      <circle cx="91" cy="46" r="41.5" fill="var(--charcoal)"/>
      <g fill="#fff">
        <polygon points="91,24 94,31 101,31 95.5,35.5 97.5,42 91,38 84.5,42 86.5,35.5 81,31 88,31"/>
        <path d="M79,40 h5 v8 a7,7 0 0 0 14,0 v-8 h5 v8 a12,12 0 0 1 -9,11.5 v5 h-6 v-5 a12,12 0 0 1 -9,-11.5 z"/>
        <rect x="82" y="66" width="18" height="5" rx="1"/>
      </g>
    </svg>
    <h2 class="value-title">Excellence</h2>
    <p class="value-text">In line with our goal, we aspire not only to alleviate pain but also to inspire patients to become active participants in their well-being. We believe in empowering our patients through education and compassion. Our pursuit of excellence is unwavering, driven by our dedication to continuously improve our services at every level, ensuring that our community receives nothing less than exceptional care.</p>
  </section>

  <section class="value value--integrity">
    <svg class="value-badge" viewBox="0 0 140 92" aria-hidden="true">
      <path d="M0,12 Q30,30 62,16 L62,76 Q30,62 0,80 Z" fill="var(--charcoal)"/>
      <circle cx="91" cy="46" r="41.5" fill="var(--charcoal)"/>
      <circle cx="91" cy="46" r="21" fill="#fff"/>
      <g stroke="var(--charcoal)" stroke-width="2.5">
        <line x1="91" y1="25" x2="91" y2="67"/><line x1="70" y1="46" x2="112" y2="46"/>
      </g>
      <g fill="var(--charcoal)"><circle cx="91" cy="36" r="3.5"/><circle cx="101" cy="46" r="3.5"/></g>
      <g fill="#fff"><circle cx="91" cy="56" r="3.5"/><circle cx="81" cy="46" r="3.5"/></g>
    </svg>
    <h2 class="value-title">Integrity</h2>
    <p class="value-text">In our healthcare team, 'Integrity' is non-negotiable.  Our purpose is deeply rooted in ethics, integrity, and professional standards. We operate with the utmost integrity in every aspect of our work, adhering to the highest ethical principles. We understand that trust is the foundation of healthcare, and we are committed to maintaining the trust our community places in us.</p>
  </section>

  <section class="value value--service">
    <svg class="value-badge" viewBox="0 0 140 92" aria-hidden="true">
      <path d="M0,12 Q30,30 62,16 L62,76 Q30,62 0,80 Z" fill="var(--charcoal)"/>
      <circle cx="91" cy="46" r="41.5" fill="var(--charcoal)"/>
      <circle cx="91" cy="46" r="19" fill="none" stroke="#fff" stroke-width="7" stroke-dasharray="7 3.2"/>
      <circle cx="91" cy="46" r="16" fill="#fff"/>
      <path d="M86,34 v8 a5,5 0 0 0 10,0 v-8 h3 v9 a8,8 0 0 1 -5,7 v12 h-6 v-12 a8,8 0 0 1 -5,-7 v-9 z" fill="var(--charcoal)"/>
    </svg>
    <h2 class="value-title">Service</h2>
    <p class="value-text">Our vision is grounded in the belief that every person possesses the innate potential for true health. We aim to facilitate the body's natural healing response by providing the highest level of service. Our hope for each patient extends beyond healing; we aspire to help you fulfill your life's mission and purpose abundantly, supporting you in your journey to well-being.</p>
  </section>

  <div class="accent-dot"></div>

  <svg class="bottom-wave" width="927" height="1200" viewBox="0 0 927 1200" aria-hidden="true">
    <path d="M386,1200 V1160 C386,1118 425,1094 470,1094 C520,1094 540,1142 594,1144 C650,1146 670,1094 719,1094 C770,1094 790,1144 829,1144 C870,1144 895,1110 927,1098 V1200 Z" fill="var(--charcoal)"/>
  </svg>
</main>
</body>
</html>
```